Local fast-growing company in the service sector

We are looking for a modern business card design, which should also appear on our letterheads

Target Market(s)

Private and industrial sectors

Contact Information for Business Card

Vorname Name
Kellbacher Str. 38
74819 Wendlingau
Tel.: 07162-418395-0
Name@service-tkwl.de

Colors
9d9d9d
919191
aaaaaa

Requirements
Must have
• The logo (file) in silver

```html
<!DOCTYPE html>
<html lang="de">
<head>
<meta charset="utf-8">
<title>TKWL Stationery</title>
<link href="https://fonts.googleapis.com/css2?family=Montserrat:wght@400;500;700&display=swap" rel="stylesheet">
<style>
:root{
  --backdrop:#ecedef;
  --paper:#ffffff;
  --ink:#1f1f1f;
  --card-dark:#141414;
  --card-mid:#262626;
  --silver:#9d9d9d;
  --silver-light:#aaaaaa;
  --silver-mid:#919191;
  --body-text:#333333;
  --soft-text:#d6d6d6;
}
*{margin:0;padding:0;box-sizing:border-box}
html,body{width:1200px;height:1000px;overflow:hidden}
body{background:var(--backdrop);font-family:"Montserrat",Arial,sans-serif;position:relative}

.letterhead{position:absolute;top:200px;width:435px;height:615px;background:var(--paper);box-shadow:3px 4px 8px rgba(0,0,0,.18);overflow:hidden}
.letterhead--blank{left:130px}
.letterhead--filled{left:626px;width:434px}
.letterhead__band{position:absolute;inset:0;background:var(--ink)}
.letterhead--blank .letterhead__band{clip-path:polygon(0 0,100% 0,100% 82px,0 178px)}
.letterhead--filled .letterhead__band{clip-path:polygon(0 0,100% 0,100% 78px,0 162px)}
.letterhead__brand{position:absolute;left:40px;top:36px;font-weight:700;font-size:42px;letter-spacing:1px;color:var(--silver);line-height:1}
.letterhead__contact{position:absolute;left:272px;top:48px;color:var(--soft-text);font-size:10.5px;line-height:13px}
.letterhead__footer{position:absolute;left:0;right:0;bottom:14px;display:flex;justify-content:center;align-items:center;gap:6px;font-size:8.5px;color:#333}
.letterhead__footer svg{width:14px;height:13px}
.letterhead__body{position:absolute;left:28px;top:208px;width:378px;font-size:5.3px;line-height:7.4px;color:var(--body-text);text-align:justify}
.letterhead__body p{margin-bottom:5px}

.business-card{position:absolute;width:250px;height:144px;color:#fff;background:linear-gradient(162deg,var(--card-dark) 0 44%,var(--card-mid) 44% 100%);box-shadow:3px 5px 10px rgba(0,0,0,.35);overflow:hidden}
.business-card--front{left:521px;top:364px;border-radius:8px}
.business-card--back{left:396px;top:525px;border-radius:2px}
.business-card__name{position:absolute;left:15px;top:16px;font-size:10.5px;font-weight:500}
.business-card__role{position:absolute;left:15px;top:29px;font-size:6.5px;color:#bdbdbd}
.business-card__contacts{position:absolute;left:15px;top:43px;list-style:none;font-size:7px;line-height:10.5px;color:#d0d0d0}
.business-card__contacts li{display:flex;align-items:center;gap:6px}
.business-card__contacts svg{width:7px;height:7px;fill:#d0d0d0}
.business-card__address{position:absolute;left:15px;top:110px;display:flex;gap:6px;font-size:7px;line-height:9px;color:#d0d0d0}
.business-card__address svg{width:8px;height:8px;margin-top:1px;fill:#d0d0d0}
.business-card__brand{position:absolute;right:16px;top:100px;font-weight:700;font-size:25px;color:var(--silver);line-height:1}
</style>
</head>
<body>

<section class="letterhead letterhead--blank">
  <div class="letterhead__band"></div>
  <div class="letterhead__brand">TKWL</div>
  <div class="letterhead__contact">07162-418395-0<br>Name@service-tkwl.de</div>
  <div class="letterhead__footer">
    <svg viewBox="0 0 14 13"><path d="M7 0 0 6.5h2V13h4V9h2v4h4V6.5h2z" fill="#1f1f1f"/></svg>
    <span>Kellbacher Str. 38, 74819 Wendlingau</span>
  </div>
</section>

<section class="letterhead letterhead--filled">
  <div class="letterhead__band"></div>
  <div class="letterhead__brand">TKWL</div>
  <div class="letterhead__contact">07162-418395-0<br>Name@service-tkwl.de</div>
  <div class="letterhead__body">
    <p>Thank you for your enquiry about our building and facility services. We are pleased to confirm that our team can take on the regular maintenance work at your site from the start of next month. All tasks will be carried out by trained and insured staff, and each visit will be recorded in a short report so that you always know exactly what has been done and when. Our site manager will contact you in the coming days to agree on a suitable schedule and to walk through the premises with you. During this visit we will also note any special wishes regarding access times, keys, cleaning agents or waste disposal. If anything changes on your side, a short call or email is enough and we will adapt our plan without delay. We value a reliable and open partnership with every client.</p>
    <p>For larger properties we offer a combined package of cleaning, caretaking and garden care. This reduces the number of contacts you need to manage and allows us to plan our staff more efficiently, which in turn keeps the price stable for you. The package can be extended at any time by winter service, window cleaning or small repair work. Every service is priced separately in the enclosed list, so you can see at a glance which items are included and which are optional. Should you wish to compare several options, we will gladly prepare a detailed offer tailored to the size and use of your building. Our team also advises you on ways to lower running costs and to keep the property in good condition over many years.</p>
    <p>Quality control is an important part of our daily work. Our supervisors check the results on site at regular intervals and speak with the staff about any points that can be improved. In addition, you will receive a short questionnaire every quarter in which you can rate our work and share your suggestions. We take every response seriously and use it to train our teams. If a problem ever arises, please contact us directly. We aim to respond within one working day and to solve the issue as quickly as possible. For urgent matters outside office hours, our emergency line is available around the clock, so that help is never far away when you need it most, whether at night or on holidays.</p>
    <p>Please note that our prices remain valid until the end of the current year. Payment is due within fourteen days of the invoice date, and all invoices are sent by email unless you prefer a printed copy. Of course, we are happy to agree on monthly billing for regular services. Any additional work will only be carried out after your written approval.</p>
    <p>We are a local company with short distances and a team that knows the region well. Over the past years we have grown steadily, and today we look after private households, offices, schools and industrial sites alike. Our staff receive regular training in safety, hygiene and the careful handling of modern equipment. We use cleaning agents that are gentle on surfaces and on the environment, and we plan our routes to avoid needless trips. This allows us to offer fair prices while keeping our promise of reliable and friendly service. We would be glad to welcome you as a new client and to show you what a dependable partner can do for your property every single day of the year.</p>
    <p>Please find our updated price list, a sample report and our general terms enclosed with this letter. If you have any questions about the documents or would like to arrange a first meeting, do not hesitate to contact us by phone or email. We are also happy to visit you on site at a time that suits you, free of charge and without obligation. Once you have decided, we will send you a written contract for your review and signature, and we can start work within a few days. We thank you for your trust and look forward to a successful and lasting cooperation. With kind regards from the whole team, and best wishes for your business and your plans in the coming months.</p>
  </div>
  <div class="letterhead__footer">
    <svg viewBox="0 0 14 13"><path d="M7 0 0 6.5h2V13h4V9h2v4h4V6.5h2z" fill="#1f1f1f"/></svg>
    <span>Kellbacher Str. 38, 74819 Wendlingau</span>
  </div>
</section>

<article class="business-card business-card--front">
  <div class="business-card__name">Vorname Name</div>
  <div class="business-card__role">Director</div>
  <ul class="business-card__contacts">
    <li><svg viewBox="0 0 10 10"><path d="M2 0 4 2.5 3 4c.8 1.4 1.6 2.2 3 3l1.5-1L10 8 8 10C4 10 0 6 0 2z"/></svg>07162-418395-0</li>
    <li><svg viewBox="0 0 10 10"><path d="M0 2h10v6H0zM0 2l5 3.5L10 2" stroke="#141414" stroke-width=".8"/></svg>Name@service-tkwl.de</li>
    <li><svg viewBox="0 0 10 10"><circle cx="5" cy="5" r="5"/></svg>service-tkwl.de</li>
  </ul>
  <div class="business-card__address">
    <svg viewBox="0 0 14 13"><path d="M7 0 0 6.5h2V13h4V9h2v4h4V6.5h2z"/></svg>
    <span>Kellbacher Str. 38<br>74819 Wendlingau</span>
  </div>
  <div class="business-card__brand">TKWL</div>
</article>

<article class="business-card business-card--back">
  <div class="business-card__name">Vorname Name</div>
  <div class="business-card__role">Director</div>
  <ul class="business-card__contacts">
    <li><svg viewBox="0 0 10 10"><path d="M2 0 4 2.5 3 4c.8 1.4 1.6 2.2 3 3l1.5-1L10 8 8 10C4 10 0 6 0 2z"/></svg>07162-418395-0</li>
    <li><svg viewBox="0 0 10 10"><path d="M0 2h10v6H0zM0 2l5 3.5L10 2" stroke="#141414" stroke-width=".8"/></svg>Name@service-tkwl.de</li>
    <li><svg viewBox="0 0 10 10"><circle cx="5" cy="5" r="5"/></svg>service-tkwl.de</li>
  </ul>
  <div class="business-card__address">
    <svg viewBox="0 0 14 13"><path d="M7 0 0 6.5h2V13h4V9h2v4h4V6.5h2z"/></svg>
    <span>Kellbacher Str. 38<br>74819 Wendlingau</span>
  </div>
  <div class="business-card__brand">TKWL</div>
</article>

</body>
</html>
```